Business Card Design Project

Design is for the business card of a holistic, integral therapist. Design is required for front (colour / pattern) and back (white, with text as below).

Please prepare the design using placeholder text. I will work with the winning submission to complete the final information in the last iteration.

To give you a sense of her services a profile is below:
- I offer an integrative approach for effective relief of many issues such as anxiety, panic attacks, relationship difficulties, and health problems. In my counselling sessions I mainly use EFT {Emotional Freedom Technique } which taps into the body's energy system (meridians) to clear up blockages and limiting /distorted thinking and beliefs. I also work on expanding awareness as well as enhancing relationships.Clients have found the sessions life changing and report feeling lighter, clearer more empowered and connected to themselves and others.

Target Market(s)

Well educated, upper socioeconomic people seeking purpose and happiness in their lives.

Industry/Entity Type

Health

Requirements
Must have
• Must have the following text on front

First Name, Last Name
LLB, ND, Dip C
Counselling & Naturopathy
Emotional Feedom Technique and Bowen Therapy

Adress 1 Line 1
Adress 1 Line 2

Adress 2 Line 1
Adress 2 Line 2

xxx.xxx@xxxxx.com

Tel: 0XXX XXX XXX

Must have the following text on reverse - which should be primarily white.

Next appointment
Date:
Time:
Nice to have
• Example colour palettes

http://www.huepinwheel.net/palette/512093/velvet_lantern
http://www.huepinwheel.net/palette/308215/Quiet_Orchard
http://www.huepinwheel.net/palette/426958/Soft_Harbor_Glow

Example images that may be useful...
http://www.brindlemart.net/gp/product/images/4719260351/ref=dp_image_text_0?ie=UTF8&n=617204&s=books
http://www.brindlemart.net/gp/customer-media/product-gallery/5280147936/ref=cm_ciu_pdp_images_all
http://en.lorewell.org/wiki/File:Lotus_Grid_256bw.gif

```html
<!DOCTYPE html>
<html lang="en">
<head>
<meta charset="utf-8">
<title>Business Card – Holistic Therapist</title>
<link rel="stylesheet" href="https://fonts.googleapis.com/css2?family=Oxygen:wght@400&display=swap">
<style>
  :root {
    --canvas: #ffffff;
    --leaf: #8dc63f;
    --leaf-light: #b4dc7e;
    --mist: rgba(190, 225, 205, 0.75);
    --bark: #7a5a3a;
    --ochre: rgba(206, 180, 52, 0.88);
    --ink: #1a1a1a;
    --peach: #fbb25a;
    --peach-soft: #fde7c9;
    --card-edge: #111111;
  }
  * { margin: 0; padding: 0; box-sizing: border-box; }
  html, body {
    width: 1200px; height: 927px; overflow: hidden;
    background: var(--canvas);
    font-family: "Oxygen", "Open Sans", sans-serif;
  }
  .canvas { position: relative; width: 1200px; height: 927px; }

  /* Front of card */
  .card-front {
    position: absolute; left: 298px; top: 89px;
    width: 497px; height: 308px;
    background: var(--leaf);
    overflow: hidden;
  }
  .front-pattern {
    position: absolute; left: 50px; top: 0; width: 400px; height: 308px;
    background: radial-gradient(circle at 55% 45%, rgba(255,255,255,0.45) 0%, rgba(255,255,255,0.25) 40%, rgba(255,255,255,0) 70%);
  }
  .front-figure {
    position: absolute; left: 270px; top: 0; width: 222px; height: 308px;
    background: linear-gradient(180deg, #f3c35a 0%, #d9a23a 35%, #a9824a 65%, #7a4e2a 100%);
    border-radius: 110px 110px 20px 20px;
    opacity: 0.9;
  }
  .contact-box {
    position: absolute; left: 29px; top: 12px; width: 195px; height: 159px;
    background: var(--mist);
    border: 1.5px solid var(--bark);
    border-radius: 16px;
    padding: 16px 0 0 16px;
    font-size: 14px; line-height: 15px; color: var(--ink);
  }
  .contact-box .group { margin-bottom: 15px; }
  .credentials-box {
    position: absolute; left: 73px; top: 183px; width: 358px; height: 111px;
    background: var(--ochre);
    border: 1.5px solid var(--bark);
    border-radius: 16px;
    padding: 12px 0 0 5px;
    font-size: 13.5px; line-height: 24px; color: var(--ink);
    white-space: nowrap;
  }

  /* Back of card */
  .card-back {
    position: absolute; left: 298px; top: 508px;
    width: 507px; height: 287px;
    border: 1.5px solid var(--card-edge);
    background: linear-gradient(180deg, #ffffff 0%, #fffaf3 60%, var(--peach-soft) 88%, var(--peach) 100%);
    overflow: hidden;
  }
  .back-pattern {
    position: absolute; left: 99px; top: 0; width: 408px; height: 287px;
    background: radial-gradient(circle at 72% 58%, rgba(251,178,90,0.35) 0%, rgba(251,178,90,0.18) 45%, rgba(251,178,90,0) 75%);
  }
  .appointment {
    position: absolute; left: 32px; top: 48px;
    font-size: 19.5px; line-height: 40px; letter-spacing: 1px; color: var(--ink);
    list-style: none;
  }
</style>
</head>
<body>
<main class="canvas">
  <section class="card-front">
    <div class="front-pattern" role="img" aria-label="Faint white sacred geometry flower pattern"></div>
    <div class="front-figure" role="img" aria-label="Illustration of a seated meditating figure with chakra colours"></div>
    <address class="contact-box">
      <p class="group">Adress 1 Line 1<br>Adress 1 Line 2</p>
      <p class="group">Adress 2 Line 1<br>Adress 2 Line 2</p>
      <p>xxx.xxx@xxxxx.com<br>Tel: 0XXX XXX XXX</p>
    </address>
    <div class="credentials-box">
      <p>First Name, Last Name</p>
      <p>LLB, ND, Dip C</p>
      <p>Counselling &amp; Naturopathy</p>
      <p>Emotional Feedom Technique and Bowen Therapy</p>
    </div>
  </section>

  <section class="card-back">
    <div class="back-pattern" role="img" aria-label="Faint orange lotus yantra line pattern"></div>
    <ul class="appointment">
      <li>Next appointment</li>
      <li>Date:</li>
      <li>Time:</li>
      <li>Nice to Have:</li>
    </ul>
  </section>
</main>
</body>
</html>
```